Webdesign für visa-korvenet.org
Kreativer Initialvorschlag, schnelle Umsetzung, flexible Anpassung des Designvorschlags und nette Kommunikation, gerne wieder!
Zielgruppe
Wir vermitteln weltweit Reisegenehmigungen für Geschäfts- und Privatkunden. Auf VISA-Korvenet.org möchten wir auf deutsch, englisch & chinesisch Reisenden bei der Beiholung von Kurzzeit, Work & Travel & diversen Visaarten helfen.
Aufgabenstellung
Der Webseitezweck ist es, dass Besucher bestellen. Dafür muss die Seite attraktiv, einfach bedienbar und das CTA Element "zum Formular" präsent und mehrfach auftauchen.

```html
<!DOCTYPE html>
<html lang="de">
<head>
<meta charset="utf-8">
<title>VISA Korvenet – Mobile Screens</title>
<link href="https://fonts.googleapis.com/css2?family=Exo+2:wght@300;400;500;600;700&display=swap" rel="stylesheet">
<style>
  :root {
    --blue: #0b4a93;
    --blue-text: #1d4f9c;
    --red: #b3121b;
    --grey: #8a8a8a;
    --grey-line: #9a9a9a;
    --footer: #a3a3a3;
    --white: #ffffff;
  }
  * { box-sizing: border-box; margin: 0; padding: 0; }
  html, body { width: 1200px; height: 2420px; overflow: hidden; background: var(--white); }
  body { position: relative; font-family: "Exo 2", sans-serif; color: var(--blue-text); }

  .screen { position: absolute; width: 321px; background: var(--white); overflow: hidden;
    box-shadow: 0 0 0 1px #e4e4e4; }
  .screen--home { left: 321px; top: 113px; height: 575px; }
  .screen--info { left: 321px; top: 925px; height: 1140px; }
  .screen--form { left: 774px; top: 925px; height: 1140px; }

  .hotline { position: absolute; left: 7px; top: 8px; display: flex; gap: 8px; color: var(--red);
    font-weight: 600; font-size: 14px; line-height: 16px; }
  .hotline em { font-weight: 500; }
  .hotline svg { margin-top: 4px; }

  .brand { position: absolute; left: 0; width: 100%; top: 52px; text-align: center; }
  .brand__name { font-size: 33px; font-weight: 700; color: var(--blue); line-height: 40px; }
  .brand__tag { font-size: 15px; font-weight: 400; color: var(--blue); line-height: 18px; }

  .nav { position: absolute; left: 0; width: 100%; height: 48px; display: flex; align-items: center; }
  .nav--line { border-bottom: 1.5px solid var(--blue); }
  .nav__figure { position: absolute; width: 26px; height: 30px; border-radius: 6px; }
  .nav__figure--traveler { left: 45px; background: var(--blue); }
  .nav__figure--traveler.is-active { background: var(--red); }
  .nav__figure--business { left: 180px; background: var(--blue); border-radius: 13px 13px 4px 4px; }
  .nav__label { position: absolute; left: 86px; color: var(--red); font-weight: 600; font-size: 15px; }
  .nav__icon { position: absolute; top: 50%; transform: translateY(-50%); }

  .hero { position: absolute; left: 0; top: 166px; width: 100%; height: 121px;
    background: linear-gradient(180deg, #2a2f3d 0%, #1b2230 55%, #4a3c2a 78%, #1a2a3a 100%); }

  .copy { position: absolute; left: 29px; width: 280px; font-size: 13px; line-height: 18px;
    font-weight: 400; color: var(--blue-text); }
  .copy strong { font-weight: 600; }
  .copy p + p { margin-top: 18px; }

  .section-title { position: absolute; left: 29px; color: var(--red); font-size: 23px; font-weight: 600; }

  .visa { position: absolute; left: 29px; width: 280px; }
  .visa__head { display: flex; gap: 4px; align-items: flex-start; }
  .visa__figure { width: 38px; height: 44px; background: var(--red); border-radius: 6px; flex: none; }
  .visa__title { font-size: 22px; font-weight: 600; color: var(--blue); line-height: 24px; white-space: nowrap; }
  .visa__sub { font-size: 13px; line-height: 16px; }
  .visa__text { font-size: 13px; line-height: 18px; margin-top: 6px; }

  .btn { position: absolute; background: var(--blue); color: var(--white); font-weight: 700;
    font-size: 22px; display: flex; align-items: center; justify-content: center; }
  .btn--register { width: 150px; height: 40px; left: 84px; }
  .btn--submit { width: 150px; height: 40px; left: 83px; top: 982px; }

  .faq { position: absolute; left: 30px; width: 276px; display: flex; justify-content: space-between;
    align-items: center; font-size: 16px; font-weight: 600; line-height: 18px; color: var(--blue); }
  .faq span b { color: var(--red); font-weight: 600; }

  .footer { position: absolute; left: 0; bottom: 0; width: 100%; height: 35px; background: var(--footer);
    color: #333; font-size: 13px; display: flex; align-items: center; justify-content: center; }

  .steps { position: absolute; left: 29px; top: 70px; font-size: 17px; font-weight: 500; line-height: 24px; color: var(--grey); }
  .steps .is-current { color: var(--red); }

  .form-head { position: absolute; left: 29px; top: 154px; }

  .field { position: absolute; left: 33px; width: 250px; height: 25px; border: 1px solid var(--grey-line);
    font-size: 13px; color: var(--grey); padding: 3px 5px; line-height: 17px; }
  .field i { color: var(--red); font-style: normal; }
  .field--select::after { content: ""; position: absolute; right: 8px; top: 8px; width: 5px; height: 5px;
    border-right: 1.3px solid #555; border-bottom: 1.3px solid #555; transform: rotate(45deg); }
  .field--short { left: 183px; width: 100px; }
  .label { position: absolute; font-size: 13px; color: var(--grey); }
  .label i { color: var(--red); font-style: normal; }

  .question { position: absolute; left: 37px; width: 246px; font-size: 13px; line-height: 19.5px; color: #444; }
  .question i { color: var(--red); font-style: normal; }
  .choice { position: absolute; display: flex; align-items: center; gap: 6px; font-size: 13px; color: #444; }
  .choice span.box { width: 24px; height: 24px; border: 1px solid var(--grey-line); display: block; }
</style>
</head>
<body>

<!-- Home screen -->
<section class="screen screen--home">
  <div class="hotline">
    <svg width="24" height="24" viewBox="0 0 24 24" fill="none" stroke="#0b4a93" stroke-width="2.2">
      <path d="M5 3l4 1 1 5-3 2c1 3 3 5 6 6l2-3 5 1 1 4c-1 2-3 3-5 2C9 19 4 14 3 7c0-2 1-4 2-4z"/>
      <path d="M14 3a7 7 0 0 1 7 7M14 7a3 3 0 0 1 3 3" stroke-linecap="round"/>
    </svg>
    <div>ServiceHotline <em>FREE</em> 0800 555 010 200<br>Mo - Fr 10-16</div>
  </div>

  <div class="brand">
    <div class="brand__name">VISA Korvenet</div>
    <div class="brand__tag">deutsche Formulare Visum Australien</div>
  </div>

  <nav class="nav" style="top:119px">
    <span class="nav__figure nav__figure--traveler" role="img" aria-label="Symbol Tourist"></span>
    <span class="nav__label">&lt; Anträge &gt;</span>
    <span class="nav__figure nav__figure--business" role="img" aria-label="Symbol Geschäftsreisender"></span>
    <svg class="nav__icon" style="left:241px" width="20" height="20" viewBox="0 0 20 20"><circle cx="10" cy="10" r="8.5" fill="none" stroke="#0b4a93" stroke-width="1.3"/><circle cx="10" cy="6" r="1.3" fill="#0b4a93"/><rect x="9" y="8.5" width="2" height="6.5" fill="#0b4a93"/></svg>
    <span class="nav__icon" style="left:271px;color:var(--blue);font-size:20px">@</span>
  </nav>

  <div class="hero" role="img" aria-label="Foto: Skyline von Sydney bei Nacht mit Einreisestempel"></div>

  <div class="copy" style="top:296px">
    <p><strong>Evisitor Visum Australien</strong> (bis 2008 ETA - Electronic Travel Authority Australia)</p>
    <p>Touristen und Geschäftsleute benötigen zur Einreise nach Australien vor Reisebeginn ein gültiges Visum, kurz „eVisitor“.Bis 2008 hieß dieses Visum noch (Electronic Travel Authority). Eine Evisitor Registrierung ist wie ein Visum zeitlich begrenzt. Sowohl Touristen wie auch Geschäftsreisende können sich mit einem gültigen Evisitor Visum 3 Monate in Australien aufhalten. Evisitor Visa haben eine Gültigkeit von 12 Monaten, somit können Reisende innerhalb eines Jahres auch mehrfach nach Australien einreisen.</p>
  </div>
</section>

<!-- Info screen -->
<section class="screen screen--info">
  <div class="copy" style="top:58px">
    <p>aufhalten. Evisitor Visa haben eine Gültigkeit von 12 Monaten, somit können Reisende innerhalb eines Jahres auch mehrfach nach Australien einreisen.</p>
  </div>

  <nav class="nav nav--line" style="top:0; background:var(--white)">
    <span class="nav__figure nav__figure--traveler" role="img" aria-label="Symbol Tourist"></span>
    <span class="nav__label">&lt; Anträge &gt;</span>
    <span class="nav__figure nav__figure--business" role="img" aria-label="Symbol Geschäftsreisender"></span>
    <svg class="nav__icon" style="left:241px" width="20" height="20" viewBox="0 0 20 20"><circle cx="10" cy="10" r="8.5" fill="none" stroke="#0b4a93" stroke-width="1.3"/><circle cx="10" cy="6" r="1.3" fill="#0b4a93"/><rect x="9" y="8.5" width="2" height="6.5" fill="#0b4a93"/></svg>
    <span class="nav__icon" style="left:271px;color:var(--blue);font-size:20px">@</span>
  </nav>

  <h2 class="section-title" style="top:141px">Unterscheidung</h2>

  <article class="visa" style="top:195px">
    <div class="visa__head">
      <span class="visa__figure" role="img" aria-label="Symbol Tourist"></span>
      <div><div class="visa__title">eVisitor „Tourist ETA“</div><div class="visa__sub">12 Monate gültig</div></div>
    </div>
    <p class="visa__text">Mit dem Visitor Visum können Touristen bis zu drei Monaten am Stück nach Australien reisen um dort Urlaub zu machen, Verwandte oder Bekannte zu besuchen. Eine arbeitsbezogene Nutzung dieses Visums ist aus- drücklich nicht gestattet!<br>Wichtig: Es muss bereits vor Antritt der Reise ein gültiges Visum vorliegen. Drucken Sie Ihre eVisitor Nummer aus und legen Sie diese Ihren Reisedokumenten bei.</p>
  </article>
  <a class="btn btn--register" style="top:441px">registrieren</a>

  <article class="visa" style="top:515px">
    <div class="visa__head">
      <span class="visa__figure" style="border-radius:18px 18px 4px 4px" role="img" aria-label="Symbol Geschäftsreisender"></span>
      <div><div class="visa__title">eVisitor „Business ETA“</div><div class="visa__sub">12 Monate gültig</div></div>
    </div>
    <p class="visa__text">Mit dem Visitor Visum können Touristen bis zu drei Monaten am Stück nach Australien reisen um dort Urlaub zu machen, Verwandte oder Bekannte zu besuchen. Eine arbeitsbezogene Nutzung dieses Visums ist aus- drücklich nicht gestattet!<br>Wichtig: Es muss bereits vor Antritt der Reise ein gültiges Visum vorliegen. Drucken Sie Ihre eVisitor Nummer aus und legen Sie diese Ihren Reisedokumenten bei.</p>
  </article>
  <a class="btn btn--register" style="top:761px">registrieren</a>

  <div class="faq" style="top:845px"><span>Welche Dokumente erhalte ich<br>mit meinem Evisitor Visum?</span><svg width="26" height="26" viewBox="0 0 26 26"><circle cx="13" cy="13" r="11.5" fill="none" stroke="#777" stroke-width="1.5"/><path d="M13 7v12M7 13h12" stroke="#777" stroke-width="2"/></svg></div>
  <div class="faq" style="top:899px"><span>Was darf man als eVisitor<br>(Inhaber eines ETA Visum) in<br>Australien machen?</span><svg width="26" height="26" viewBox="0 0 26 26"><circle cx="13" cy="13" r="11.5" fill="none" stroke="#777" stroke-width="1.5"/><path d="M13 7v12M7 13h12" stroke="#777" stroke-width="2"/></svg></div>
  <div class="faq" style="top:971px"><span>3 Tipps für eine erfolgreiche<br>Australien Reise</span><svg width="26" height="26" viewBox="0 0 26 26"><circle cx="13" cy="13" r="11.5" fill="none" stroke="#777" stroke-width="1.5"/><path d="M13 7v12M7 13h12" stroke="#777" stroke-width="2"/></svg></div>
  <div class="faq" style="top:1025px"><span>Übersicht Ihrer Vorteile mit<br>uns von <b>visa-korvenet.org</b></span><svg width="26" height="26" viewBox="0 0 26 26"><circle cx="13" cy="13" r="11.5" fill="none" stroke="#777" stroke-width="1.5"/><path d="M13 7v12M7 13h12" stroke="#777" stroke-width="2"/></svg></div>

  <footer class="footer">FOOTER</footer>
</section>

<!-- Form screen -->
<section class="screen screen--form">
  <nav class="nav nav--line" style="top:0">
    <span class="nav__figure nav__figure--traveler is-active" role="img" aria-label="Symbol Tourist"></span>
    <span class="nav__label">&lt; Anträge &gt;</span>
    <span class="nav__figure nav__figure--business" role="img" aria-label="Symbol Geschäftsreisender"></span>
    <svg class="nav__icon" style="left:241px" width="20" height="20" viewBox="0 0 20 20"><circle cx="10" cy="10" r="8.5" fill="none" stroke="#0b4a93" stroke-width="1.3"/><circle cx="10" cy="6" r="1.3" fill="#0b4a93"/><rect x="9" y="8.5" width="2" height="6.5" fill="#0b4a93"/></svg>
    <span class="nav__icon" style="left:271px;color:var(--blue);font-size:20px">@</span>
  </nav>

  <ol class="steps" style="list-style:none">
    <li class="is-current">1. Formular ausfüllen</li>
    <li>2. Antrag überprüfen</li>
    <li>3. Bezahlen</li>
  </ol>

  <div class="visa form-head">
    <div class="visa__head">
      <span class="visa__figure" role="img" aria-label="Symbol Tourist"></span>
      <div><div class="visa__title">eVisitor „Tourist ETA“</div><div class="visa__sub">12 Monate gültig</div></div>
    </div>
  </div>

  <div class="field" style="top:226px">Nachname<i>*</i></div>
  <div class="field" style="top:264px">Vorname<i>*</i></div>
  <div class="field" style="top:302px">Früherer Name</div>
  <svg style="position:absolute;left:287px;top:303px" width="20" height="20" viewBox="0 0 20 20"><circle cx="10" cy="10" r="8.5" fill="none" stroke="#b3121b" stroke-width="1.3"/><circle cx="10" cy="6" r="1.3" fill="#b3121b"/><rect x="9" y="8.5" width="2" height="6.5" fill="#b3121b"/></svg>

  <span class="label" style="left:38px;top:344px">Geburtstag<i>*</i></span>
  <span class="label" style="left:134px;top:344px">Tag</span>
  <div class="field field--select field--short" style="top:340px"></div>
  <span class="label" style="left:133px;top:383px">Monat</span>
  <div class="field field--select field--short" style="top:379px"></div>
  <span class="label" style="left:133px;top:421px">Jahr</span>
  <div class="field field--select field--short" style="top:417px"></div>

  <div class="field field--select" style="top:482px">Geburtsland<i>*</i></div>
  <div class="field field--select" style="top:520px">Staatsangehörigkeit<i>*</i></div>
  <div class="field field--select" style="top:558px">Geschlecht<i>*</i></div>

  <p class="question" style="top:604px">Sind Sie frei von Tuberkulose zum Antritt der Reise, bzw. bei der Einreise nach Australien?<i>*</i></p>
  <div class="choice" style="left:154px;top:657px">JA <span class="box"></span></div>
  <div class="choice" style="left:221px;top:657px">NEIN <span class="box"></span></div>

  <p class="question" style="top:701px">Haben Sie schon einmal eine oder mehrere Straftaten begangen, für die Sie eine Gesamtstrafdauer von 12 Monaten oder mehr, auf Bewährung oder nicht auf Bewährung, verbüßen mussten?<i>*</i></p>
  <div class="choice" style="left:154px;top:814px">JA <span class="box"></span></div>
  <div class="choice" style="left:221px;top:814px">NEIN <span class="box"></span></div>

  <p class="question" style="top:856px">Sind Sie frei von Tuberkulose zum Antritt der Reise, bzw. bei der Einreise nach Australien?<i>*</i></p>
  <div class="choice" style="left:154px;top:909px">JA <span class="box"></span></div>
  <div class="choice" style="left:221px;top:909px">NEIN <span class="box"></span></div>

  <a class="btn btn--submit">Abschicken</a>

  <footer class="footer">FOOTER</footer>
</section>

</body>
</html>
```